Business Cards for a law firm

Business cards for our law firm. Use our silhoette logo and OAK HARBOR - check our website (www.oakharbor-legal.com)

Contact Information for Business Card

our silhouette logo, OAK HARBOR, 800-555-0147, Dorian Kestrup, dorian@oakharbor-legal.com

Requirements
Must have
• our silhouette logo, OAK HARBOR, 800-555-0147, Dorian Kestrup, dorian@oakharbor-legal.com

```html
<!DOCTYPE html>
<html lang="en">
<head>
<meta charset="utf-8">
<title>Oak Harbor – Business Card</title>
<link href="https://fonts.googleapis.com/css2?family=Jost:wght@500;600&family=Open+Sans:wght@400&display=swap" rel="stylesheet">
<style>
  :root {
    --ink: #333333;
    --orange: #f7904a;
    --navy: #0d3f7d;
    --blue: #1f73cc;
    --bright-blue: #1e80da;
    --cyan: #1ab0f0;
    --paper: #ffffff;
  }
  html, body {
    margin: 0;
    padding: 0;
    overflow: hidden;
    background: var(--paper);
  }
  .card {
    position: relative;
    width: 1200px;
    height: 705px;
    overflow: hidden;
    background: var(--paper);
  }
  .card__waves {
    position: absolute;
    inset: 0;
    width: 1200px;
    height: 705px;
  }
  .brand {
    position: absolute;
    left: 72px;
    top: 118px;
  }
  .brand__name {
    margin: 0;
    font-family: "Jost", sans-serif;
    font-weight: 500;
    font-size: 66px;
    line-height: 1;
    letter-spacing: 1px;
    color: var(--ink);
  }
  .brand__tagline {
    margin: 12px 0 0;
    font-family: "Jost", sans-serif;
    font-weight: 600;
    font-size: 32px;
    line-height: 1;
    letter-spacing: 0.5px;
    color: var(--orange);
  }
  .brand__rule {
    position: absolute;
    left: 72px;
    top: 246px;
    width: 99px;
    height: 3px;
    background: linear-gradient(90deg, var(--navy), var(--blue));
  }
  .contact {
    position: absolute;
    left: 71px;
    top: 294px;
    margin: 0;
    padding: 0;
    list-style: none;
  }
  .contact__item {
    display: flex;
    align-items: flex-start;
    height: 82px;
  }
  .contact__icon {
    width: 62px;
    height: 62px;
    flex: none;
    margin-right: 21px;
  }
  .contact__text {
    font-family: "Open Sans", sans-serif;
    font-weight: 400;
    font-size: 24px;
    line-height: 1;
    color: var(--ink);
    padding-top: 4px;
  }
  .emblem {
    position: absolute;
    left: 671px;
    top: 143px;
    width: 356px;
    height: 356px;
    border-radius: 50%;
    border: 17px solid var(--orange);
    background: var(--paper);
    display: flex;
    align-items: center;
    justify-content: center;
  }
  .emblem__name {
    font-family: "Jost", sans-serif;
    font-weight: 500;
    font-size: 44px;
    letter-spacing: 1px;
    color: var(--navy);
  }
</style>
</head>
<body>
<main class="card">
  <svg class="card__waves" viewBox="0 0 1004 590" preserveAspectRatio="none" aria-hidden="true">
    <defs>
      <linearGradient id="navyWave" x1="0" y1="0" x2="1" y2="0">
        <stop offset="0" stop-color="#0d3f7d"/>
        <stop offset="1" stop-color="#1f73cc"/>
      </linearGradient>
      <linearGradient id="brightWave" x1="0" y1="0" x2="1" y2="0">
        <stop offset="0" stop-color="#1560bd"/>
        <stop offset="1" stop-color="#1e80da"/>
      </linearGradient>
    </defs>
    <path class="wave wave--bright" fill="url(#brightWave)"
      d="M380 590 C480 480 600 420 760 382 C880 352 960 360 1004 372 L1004 590 Z"/>
    <path class="wave wave--orange" fill="#f7904a"
      d="M150 590 C320 470 540 385 760 340 C880 315 960 320 1004 335 L1004 372 C960 360 880 352 760 382 C600 422 480 482 380 590 Z"/>
    <path class="wave wave--navy" fill="url(#navyWave)"
      d="M0 490 C150 530 300 460 420 390 C560 310 720 270 880 262 C950 260 985 280 1004 292 L1004 336 C960 320 880 315 760 340 C540 385 320 470 150 590 L0 590 Z"/>
    <path class="wave wave--accent" fill="none" stroke="#1ab0f0" stroke-width="6" stroke-linecap="round"
      d="M520 594 C580 530 640 482 705 452"/>
  </svg>

  <header class="brand">
    <h1 class="brand__name">OAK HARBOR</h1>
    <p class="brand__tagline">Injury Attorneys</p>
  </header>
  <div class="brand__rule"></div>

  <ul class="contact">
    <li class="contact__item">
      <svg class="contact__icon" viewBox="0 0 62 62" aria-hidden="true">
        <defs>
          <linearGradient id="iconFill" x1="0" y1="0" x2="1" y2="1">
            <stop offset="0" stop-color="#0d3f7d"/>
            <stop offset="1" stop-color="#1f73cc"/>
          </linearGradient>
        </defs>
        <circle cx="31" cy="31" r="31" fill="url(#iconFill)"/>
        <path fill="#fff" d="M22 17c1.5-1 3-.6 3.8.8l2.8 4.8c.7 1.2.4 2.5-.6 3.3l-2 1.6c1.4 3.4 4 6 7.4 7.6l1.7-2c.9-1 2.2-1.2 3.3-.5l4.7 3c1.3.8 1.6 2.4.7 3.7l-1.8 2.4c-1.2 1.6-3.3 2.1-5.2 1.4C28.7 41 21 33.3 18.6 25.2c-.6-2 0-4.1 1.6-5.3z"/>
      </svg>
      <span class="contact__text">800-555-0147</span>
    </li>
    <li class="contact__item">
      <svg class="contact__icon" viewBox="0 0 62 62" aria-hidden="true">
        <circle cx="31" cy="31" r="31" fill="url(#iconFill)"/>
        <g fill="none" stroke="#fff" stroke-width="2.2">
          <circle cx="30" cy="30" r="12"/>
          <ellipse cx="30" cy="30" rx="5.5" ry="12"/>
          <path d="M18 30h24M20 23.5h20M20 36.5h20"/>
        </g>
        <path fill="#fff" stroke="#1a5fae" stroke-width="1.2" d="M35 34l9 3.5-3.8 1.6 2.8 3.6-1.8 1.4-2.8-3.6-2 3.4z"/>
      </svg>
      <span class="contact__text">dorian@oakharbor-legal.com</span>
    </li>
    <li class="contact__item">
      <svg class="contact__icon" viewBox="0 0 62 62" aria-hidden="true">
        <circle cx="31" cy="31" r="31" fill="url(#iconFill)"/>
        <path fill="#fff" d="M31 15c-6 0-10.5 4.6-10.5 10.4C20.5 33 31 46 31 46s10.5-13 10.5-20.6C41.5 19.6 37 15 31 15zm0 14.6a4.2 4.2 0 1 1 0-8.4 4.2 4.2 0 0 1 0 8.4z"/>
      </svg>
      <span class="contact__text">Dorian Kestrup</span>
    </li>
  </ul>

  <div class="emblem">
    <span class="emblem__name">OAK HARBOR</span>
  </div>
</main>
</body>
</html>
```